Quorvane Capital Modern Business Card

We need a modern business card template designed for Quorvane Capital.
Quorvane Capital is a diversified global cryptocurrency investment fund.

The font under the logo: Hiragino Kaku Gothic Pro

Color Hexcode: Main colors white (ffffff) & teal (188383), we are open to adding #fcca46 as an accent

Target Market(s)

Accredited Investors, high net worth individuals and institutional investors

Industry/Entity Type

Investment

Contact Information for Business Card

Contact Information should contain
Name
main phone +1 720 555 0147
cell
email

Font styles to use
Sans Serif
Other font styles liked:
• Hiragino Kaku Gothic Pro

Requirements
Must have
• would like to have icons that identify the contact information
• include our website: www.quorvanecapital.example
• include our Tagline: Diversified Crypto Investment Funds
Nice to have
• Would like to have a simple back side with the logo (without the words) and plenty of space

```html
<!DOCTYPE html>
<html lang="en">
<head>
<meta charset="utf-8">
<title>Quorvane Capital – Business Card</title>
<link rel="stylesheet" href="https://fonts.googleapis.com/css2?family=Open+Sans:wght@400;600&display=swap">
<style>
  :root {
    --teal: #1e9494;
    --white: #ffffff;
    --backdrop: #c9c9c7;
    --shadow: rgba(0, 0, 0, 0.35);
  }
  * { margin: 0; padding: 0; box-sizing: border-box; }
  html, body {
    width: 1200px;
    height: 1000px;
    overflow: hidden;
  }
  body {
    position: relative;
    background: var(--backdrop);
    font-family: "Open Sans", Arial, sans-serif;
  }
  .card {
    position: absolute;
    border-radius: 28px;
    overflow: hidden;
    box-shadow: 0 8px 14px var(--shadow);
  }

  /* Back side */
  .card-back {
    left: 148px; top: 100px;
    width: 631px; height: 359px;
    background: var(--white);
    display: flex;
    align-items: center;
    justify-content: center;
  }
  .card-back .brand-name {
    color: var(--teal);
    font-weight: 600;
    font-size: 40px;
    letter-spacing: 4px;
    text-transform: uppercase;
  }

  /* Front side */
  .card-front {
    left: 372px; top: 547px;
    width: 634px; height: 362px;
    background: var(--teal);
    color: var(--white);
  }
  .person-name {
    position: absolute;
    left: 28px; top: 104px;
    font-size: 28px;
    font-weight: 400;
    letter-spacing: 1.5px;
  }
  .brand-block {
    position: absolute;
    left: 330px; top: 88px;
    width: 290px;
    text-align: center;
  }
  .brand-block .brand-name {
    font-size: 15px;
    font-weight: 400;
    letter-spacing: 1px;
    text-transform: uppercase;
  }
  .brand-block .tagline {
    margin-top: 2px;
    font-size: 16px;
  }
  .divider {
    position: absolute;
    left: 0; top: 0;
  }
  .website {
    position: absolute;
    left: 380px; top: 180px;
    width: 236px;
    text-align: center;
    color: var(--teal);
    font-size: 16px;
    font-weight: 600;
  }
  .contact-list {
    position: absolute;
    left: 68px; top: 226px;
    list-style: none;
  }
  .contact-list li {
    display: flex;
    align-items: center;
    height: 34px;
    font-size: 22px;
    letter-spacing: 1.2px;
  }
  .contact-list .icon {
    width: 26px; height: 22px;
    margin-right: 20px;
    fill: var(--white);
  }
</style>
</head>
<body>

  <section class="card card-back" aria-label="Card back">
    <span class="brand-name">Quorvane Capital</span>
  </section>

  <section class="card card-front" aria-label="Card front">
    <svg class="divider" width="634" height="362" viewBox="0 0 634 362" aria-hidden="true">
      <rect x="0" y="174" width="340" height="3" fill="#ffffff"/>
      <path d="M328 180 H634 V205 H352 Q340 205 336 196 Z" fill="#ffffff"/>
    </svg>

    <h1 class="person-name">Name of Person</h1>

    <div class="brand-block">
      <div class="brand-name">Quorvane Capital</div>
      <div class="tagline">Diversified Crypto Investment Funds</div>
    </div>

    <div class="website">www.quorvanecapital.example</div>

    <ul class="contact-list">
      <li>
        <svg class="icon" viewBox="0 0 26 22" aria-hidden="true">
          <path d="M2 6 Q13 -1 24 6 L22 9 L18 8 L18 5 Q13 3 8 5 L8 8 L4 9 Z"/>
          <path d="M6 10 H20 L23 20 H3 Z"/>
          <circle cx="13" cy="15" r="3.2" fill="#1e9494"/>
        </svg>
        <span>+1 720 555 0147</span>
      </li>
      <li>
        <svg class="icon" viewBox="0 0 26 22" aria-hidden="true">
          <path d="M7 2 L10 2 L12 7 L9.5 9 Q11 13 15 15 L17 12.5 L22 14.5 L22 18 Q20 21 16 20 Q7 17 4 7 Q4 3 7 2 Z"/>
        </svg>
        <span>+ 0 000 000 0000</span>
      </li>
      <li>
        <svg class="icon" viewBox="0 0 26 22" aria-hidden="true">
          <path d="M3 5 H23 L13 12 Z"/>
          <path d="M3 7.5 L13 14.5 L23 7.5 V17 H3 Z"/>
        </svg>
        <span>name@quorvanecapital.example</span>
      </li>
    </ul>
  </section>

</body>
</html>
```